Commercial HVAC and Refrigeration Business cards

Frost-Haven Company is looking for flashy new business cards! We design, install, service and maintain commercial refrigeration, air conditioning, heating and refrigeration equipment. Our colors are blue and white. I'm open to single and double sided designs. Each employee will have their own business card. I've attached a copy of our current logo.

Our website, office and cell phone (cell phone is optional), email address should be clearly legible. "24 Hour Service" and the services we offer are; Sales, Service, Design, Installation, Maintenance. Refrigeration, Heating, Air Conditioning, Ice Machines. Does not have to be in any order.

Target Market(s)

Commercial; Restaurants, hotels, bars, breweries etc.

Industry/Entity Type

Hvac

Contact Information for Business Card

Name; Job Title, Phone Number, Email Address. www.frost-haven-example.com 24 Hour Service. We provide - Sales, Design, Installation, Service, Maintenance. We service - Refrigeration, Heating, Air Conditioning, Ice Machines

Font styles to use
Other font styles liked:
• Be creative

Colors
0255a3
ffffff

Requirements
Must have
• Professional appearance and appeal to commercial clients in the food-service and hospitality industry. Must be clearly legible and easy to understand.
Nice to have
• We want to sell maintenance agreements, perhaps we can use the back of the card to tie into a webpage about our maintenance agreements.
Should not have
• Cartoons or unprofessional. Nothing too edgy.

```html
<!DOCTYPE html>
<html lang="en">
<head>
<meta charset="utf-8">
<title>Frost-Haven Company – Business Cards</title>
<link rel="stylesheet" href="https://fonts.googleapis.com/css2?family=Open+Sans:wght@400;600;700&display=swap">
<style>
  :root {
    --brand-blue: #0255a3;
    --card-blue: #06427f;
    --white: #ffffff;
    --ink: #1d1d1f;
    --wash: #e9eef5;
    --page: #eceff3;
  }
  * { box-sizing: border-box; margin: 0; padding: 0; }
  html, body { width: 1200px; height: 900px; overflow: hidden; }
  body {
    background: var(--page);
    font-family: "Open Sans", Arial, sans-serif;
    position: relative;
  }
  .card {
    position: absolute;
    width: 560px;
    height: 320px;
    border-radius: 4px;
    overflow: hidden;
    box-shadow: 0 6px 18px rgba(0,0,0,.18);
  }
  /* Back of card */
  .card-back { left: 60px; top: 110px; background: var(--card-blue); color: var(--white); }
  .brand-plate {
    position: absolute;
    display: flex; align-items: center; justify-content: center;
    font-weight: 700; white-space: nowrap;
    border-radius: 6px;
  }
  .card-back .brand-plate {
    right: 36px; top: 34px; width: 230px; height: 56px;
    background: var(--white); color: var(--card-blue); font-size: 21px;
  }
  .services { position: absolute; left: 40px; top: 150px; }
  .services h2 { font-size: 19px; font-weight: 600; letter-spacing: .5px; margin-bottom: 6px; }
  .services ul { list-style: none; display: flex; flex-wrap: wrap; font-size: 14.5px; margin-bottom: 18px; }
  .services li { display: flex; align-items: center; }
  .services li + li::before {
    content: ""; width: 7px; height: 7px; border-radius: 50%;
    background: var(--white); margin: 0 10px;
  }
  /* Front of card */
  .card-front { left: 580px; top: 470px; background: var(--white); color: var(--ink); }
  .watermark {
    position: absolute; left: 250px; top: 120px;
    font-size: 70px; font-weight: 700; color: var(--wash);
    transform: rotate(-62deg); transform-origin: left top; white-space: nowrap;
    top: 330px; left: 250px;
  }
  .card-front .brand-plate {
    left: 32px; top: 44px; width: 240px; height: 66px;
    background: var(--brand-blue); color: var(--white); font-size: 21px;
  }
  .contact { position: absolute; left: 322px; top: 38px; font-size: 12.5px; }
  .contact .name { color: var(--brand-blue); font-size: 17px; font-weight: 600; }
  .contact .role { font-size: 12px; margin-bottom: 20px; }
  .contact-line { display: flex; align-items: center; gap: 8px; margin-bottom: 4px; }
  .contact-line svg { width: 11px; height: 11px; fill: var(--brand-blue); flex: none; }
  .address { margin: 16px 0 6px; padding-left: 19px; line-height: 1.25; }
  .tagline { color: var(--brand-blue); font-size: 19px; font-weight: 600; padding-left: 22px; }
</style>
</head>
<body>
  <section class="card card-back">
    <div class="brand-plate">Frost-Haven Company</div>
    <div class="services">
      <h2>WE PROVIDE</h2>
      <ul><li>Sales</li><li>Design</li><li>Installation</li><li>Service</li><li>Maintenance.</li></ul>
      <h2>WE SERVICE</h2>
      <ul><li>Refrigeration</li><li>Heating</li><li>Air Conditioning</li><li>Ice Machines</li></ul>
    </div>
  </section>

  <section class="card card-front">
    <div class="watermark" aria-hidden="true">Frost-Haven Company</div>
    <div class="brand-plate">Frost-Haven Company</div>
    <div class="contact">
      <p class="name">Daniel Mercer</p>
      <p class="role">Managing Director</p>
      <p class="contact-line">
        <svg viewBox="0 0 24 24" aria-hidden="true"><path d="M6.6 10.8a15.1 15.1 0 0 0 6.6 6.6l2.2-2.2a1 1 0 0 1 1-.25 11.4 11.4 0 0 0 3.6.57 1 1 0 0 1 1 1V20a1 1 0 0 1-1 1A17 17 0 0 1 3 4a1 1 0 0 1 1-1h3.5a1 1 0 0 1 1 1c0 1.25.2 2.45.57 3.57a1 1 0 0 1-.25 1z"/></svg>
        (044)-456-7890
      </p>
      <p class="contact-line">
        <svg viewBox="0 0 24 24" aria-hidden="true"><path d="M2 5h20v14H2z M2 5l10 8 10-8" fill="none" stroke="#0255a3" stroke-width="2.5"/></svg>
        info@youremail.com
      </p>
      <p class="contact-line">
        <svg viewBox="0 0 24 24" aria-hidden="true"><circle cx="12" cy="12" r="10"/></svg>
        www.frost-haven-example.com
      </p>
      <p class="address">12345, Address Goes Here<br>Country Name, 123456</p>
      <p class="tagline">24 Hour Service</p>
    </div>
  </section>
</body>
</html>
```